Wedding Invitation and Logo

We would like an invitation and logo designed for our wedding on October 19, 2019 in Charlotte, NC. Our names are Tessa and Boyd, we met in school at Kellridge Plains University, and we got engaged at a fire tower which has a view down to the campus. You do not have to include these, but some ideas for the invitation design would be mountains, a fire tower, our initials, or the city. The wedding will be at 4:30 in the afternoon with a reception to follow. We do not need to list the families as there are four of them and that is too much info. The colors we would like to use are white, black, royal blue, and maybe silver. Do not feel obligated to use them all though.We would like the logo to include similar elements such as mountains, fire tower, or our initials(T and B). The logo can be a one color design as we may use it on our cake, as light filters to be displayed on the walls at our reception, or as an accent on name plates and stationery.We like simple, clean designs and our wedding will have a wintery theme (white linens, white chair covers, silver and royal blue accents, etc.).Things we do not want: snowflakes, flowers, polka dots, leaves, gold foil.Thank you!

Font styles to use
Serif
Script

Requirements
Must have
• Some combination of white, black, royal blue, optionally silver.
Nice to have
• Mountains, fire tower, our initials (T and B), wintry theme (no snowflakes)
Should not have
• Snowflakes, flowers, polka dots, leaves, gold foil

```html
<!DOCTYPE html>
<html lang="en">
<head>
<meta charset="utf-8">
<title>Tessa and Boyd — Wedding Invitation and Monogram Card</title>
<link href="https://fonts.googleapis.com/css2?family=Sacramento&family=Lora:wght@400;500&display=swap" rel="stylesheet">
<style>
  :root {
    --backdrop: #8d9bb5;
    --paper: #ffffff;
    --royal: #27339a;
    --silver: #b9bcc2;
    --foliage: #7f97ad;
    --foliage-soft: #b7c4d4;
  }
  html, body {
    margin: 0;
    padding: 0;
    overflow: hidden;
    background: var(--backdrop);
  }
  .canvas {
    position: relative;
    width: 1200px;
    height: 1200px;
    overflow: hidden;
    background: var(--backdrop);
  }
  .card {
    position: absolute;
    background: var(--paper);
    box-shadow: 3px 4px 6px rgba(40, 50, 80, 0.35);
  }
  .card svg { display: block; }
  .invitation { left: 77px; top: 162px; width: 634px; height: 876px; }
  .monogram-card { left: 779px; top: 432px; width: 349px; height: 336px; }

  .script { font-family: "Sacramento", cursive; fill: var(--royal); }
  .serif { font-family: "Lora", Georgia, serif; fill: var(--royal); }
  .caps { letter-spacing: 1.6px; }
  .rule { stroke: var(--royal); stroke-width: 1.4; }
</style>
</head>
<body>
<div class="canvas">

  <svg width="0" height="0" style="position:absolute" aria-hidden="true">
    <defs>
      <radialGradient id="wreath-tone" cx="0.5" cy="0.5" r="0.5">
        <stop offset="0" stop-color="var(--paper)" stop-opacity="0"/>
        <stop offset="0.58" stop-color="var(--paper)" stop-opacity="0"/>
        <stop offset="0.7" stop-color="var(--foliage-soft)" stop-opacity="0.8"/>
        <stop offset="0.8" stop-color="var(--foliage)" stop-opacity="0.75"/>
        <stop offset="0.92" stop-color="var(--silver)" stop-opacity="0.45"/>
        <stop offset="1" stop-color="var(--silver)" stop-opacity="0"/>
      </radialGradient>
      <symbol id="crest" viewBox="0 0 634 620">
        <circle role="img" aria-label="Eucalyptus wreath inside a silver geometric frame"
                cx="319" cy="310" r="268" fill="url(#wreath-tone)"/>
        <text class="script" x="322" y="270" text-anchor="middle" font-size="150">Tessa</text>
        <text class="serif caps" x="319" y="301" text-anchor="middle" font-size="12">AND</text>
        <text class="script" x="316" y="424" text-anchor="middle" font-size="160">Boyd</text>
      </symbol>
    </defs>
  </svg>

  <section class="card invitation">
    <svg width="634" height="876" viewBox="0 0 634 876">
      <use href="#crest" x="0" y="0" width="634" height="620"/>
      <text class="serif caps" x="313" y="609" text-anchor="middle" font-size="13">INVITE YOU TO JOIN IN THE CELEBRATION OF THEIR</text>
      <text class="script" x="336" y="655" text-anchor="middle" font-size="50">Wedding</text>

      <text class="serif caps" x="176" y="716" text-anchor="middle" font-size="13">AT HALF PAST FOUR</text>
      <line class="rule" x1="120" y1="730" x2="235" y2="730"/>
      <text class="serif caps" x="176" y="758" text-anchor="middle" font-size="13">IN THE AFTERNOON</text>

      <line class="rule" x1="276" y1="687" x2="276" y2="775"/>
      <text class="serif caps" x="334" y="695" text-anchor="middle" font-size="13">OCTOBER</text>
      <text class="serif" x="334" y="744" text-anchor="middle" font-size="46">19</text>
      <text class="serif" x="334" y="776" text-anchor="middle" font-size="24">2019</text>
      <line class="rule" x1="394" y1="687" x2="394" y2="775"/>

      <text class="serif caps" x="474" y="714" text-anchor="middle" font-size="13">CHARLOTTE</text>
      <line class="rule" x1="426" y1="730" x2="513" y2="730"/>
      <text class="serif caps" x="474" y="756" text-anchor="middle" font-size="13">NORTH CAROLINA</text>

      <text class="serif caps" x="318" y="812" text-anchor="middle" font-size="13">DINNER AND DANCING TO FOLLOW</text>
    </svg>
  </section>

  <section class="card monogram-card">
    <svg width="349" height="336" viewBox="0 0 349 336">
      <use href="#crest" x="0" y="0" width="349" height="341"/>
    </svg>
  </section>

</div>
</body>
</html>
```